Business Card Design Project

We need a new business card design to go along with the look of our new website. tolvarex.com We manufacture after market woodworking machinery parts. Please take a look at the colors on our website and use the same.

Industry/Entity Type

Woodworking

```html
<!DOCTYPE html>
<html lang="en">
<head>
<meta charset="utf-8">
<title>Tolvarex Parts Inc. — Business Card</title>
<link href="https://fonts.googleapis.com/css2?family=Open+Sans:wght@400;600&family=Oswald:wght@700&display=swap" rel="stylesheet">
<style>
  :root {
    --page-bg: #e9e6e1;
    --card-dark: #0f3a12;
    --card-darker: #0a2c0c;
    --brand-green: #2b9a3b;
    --brand-green-bright: #3aa847;
    --text-light: #ffffff;
    --text-soft: #d9e6d9;
    --divider: #4e8a52;
  }
  html, body {
    margin: 0;
    padding: 0;
    width: 1200px;
    height: 453px;
    overflow: hidden;
    background: var(--page-bg);
    font-family: "Open Sans", Arial, sans-serif;
  }
  .canvas {
    position: relative;
    width: 1200px;
    height: 453px;
  }
  .card {
    position: absolute;
    top: 72px;
    width: 543px;
    height: 309px;
    border-radius: 14px;
    background: linear-gradient(180deg, var(--card-dark) 0%, var(--card-darker) 100%);
    overflow: hidden;
    box-shadow: 0 4px 10px rgba(0,0,0,0.25);
  }
  .card--front { left: 47px; }
  .card--back { left: 610px; }

  .brand {
    position: absolute;
    display: flex;
    align-items: center;
    gap: 10px;
    color: var(--brand-green-bright);
    font-family: "Oswald", "Arial Narrow", sans-serif;
    font-weight: 700;
    text-transform: uppercase;
    white-space: nowrap;
  }
  .brand__dot {
    border-radius: 50%;
    background: var(--brand-green-bright);
    flex: none;
  }
  .card--front .brand {
    left: 46px;
    top: 130px;
    font-size: 25px;
  }
  .card--front .brand__dot { width: 22px; height: 22px; }

  .divider {
    position: absolute;
    left: 334px;
    top: 55px;
    width: 1px;
    height: 146px;
    background: linear-gradient(180deg, transparent, var(--divider) 20%, var(--divider) 80%, transparent);
  }
  .person {
    position: absolute;
    left: 357px;
    top: 50px;
    color: var(--text-light);
  }
  .person__name {
    margin: 0;
    font-size: 15px;
    font-weight: 600;
    letter-spacing: 0.2px;
  }
  .person__title {
    margin: 2px 0 0;
    font-size: 12.5px;
    color: var(--text-soft);
  }
  .contact {
    position: absolute;
    left: 357px;
    top: 103px;
    margin: 0;
    padding: 0;
    list-style: none;
    color: var(--text-light);
    font-size: 12px;
  }
  .contact__item {
    display: flex;
    align-items: center;
    gap: 6px;
    height: 16.5px;
  }
  .contact__icon {
    width: 9px;
    height: 9px;
    fill: var(--brand-green-bright);
    flex: none;
  }
  .address-band {
    position: absolute;
    left: 0;
    right: 0;
    bottom: 0;
    height: 35px;
    background: var(--brand-green);
    border-top: 3px solid #3a3a3a;
    color: var(--text-light);
    font-size: 12.5px;
    line-height: 33px;
    padding-left: 37px;
  }

  .card--back .brand {
    left: 0;
    right: 0;
    top: 118px;
    justify-content: center;
    font-size: 32px;
  }
  .card--back .brand__dot { width: 28px; height: 28px; }
  .card--back .website {
    position: absolute;
    left: 0;
    right: 0;
    top: 218px;
    text-align: center;
    color: var(--text-light);
    font-size: 12.5px;
    letter-spacing: 2.5px;
  }
</style>
</head>
<body>
<main class="canvas">
  <section class="card card--front">
    <div class="brand"><span class="brand__dot"></span>Tolvarex Parts Inc.</div>
    <div class="divider"></div>
    <div class="person">
      <p class="person__name">YOUR NAME</p>
      <p class="person__title">Title</p>
    </div>
    <ul class="contact">
      <li class="contact__item">
        <svg class="contact__icon" viewBox="0 0 10 10"><path d="M2 0.5 L4 2.8 L3 4 Q4.3 6 6 7 L7.2 6 L9.5 8 L8 9.6 Q3.5 9 0.4 2 Z"/></svg>877.431.5098 TF</li>
      <li class="contact__item">
        <svg class="contact__icon" viewBox="0 0 10 10"><path d="M2 0.5 L4 2.8 L3 4 Q4.3 6 6 7 L7.2 6 L9.5 8 L8 9.6 Q3.5 9 0.4 2 Z"/></svg>909.327.4461</li>
      <li class="contact__item">
        <svg class="contact__icon" viewBox="0 0 10 10"><rect x="2" y="0.5" width="6" height="3"/><rect x="0.5" y="3.5" width="9" height="4"/><rect x="2" y="7" width="6" height="2.5"/></svg>909.248.7730</li>
      <li class="contact__item">
        <svg class="contact__icon" viewBox="0 0 10 10"><rect x="0.5" y="2" width="9" height="6.5"/></svg>Sales@Tolvarex.com</li>
      <li class="contact__item">
        <svg class="contact__icon" viewBox="0 0 10 10"><circle cx="5" cy="5" r="4.5"/></svg>www.tolvarex.com</li>
    </ul>
    <div class="address-band">Tolvarex Parts&nbsp; 2870 Larkspur Ridge Road #312&nbsp; Fenwick CA 91802&nbsp; USA</div>
  </section>

  <section class="card card--back">
    <div class="brand"><span class="brand__dot"></span>Tolvarex Parts Inc.</div>
    <div class="website">www.tolvarex.com</div>
  </section>
</main>
</body>
</html>
```